Agricultural Commodities Specialist Needs a Business Card Design

Business owner Rob Tenwick, need a business card design for his company based in Brisbane, Australia called "RT Harvestline Pty Ltd".
Rob is an Agricultural Commodities Specialist:
-Specialising in Domestic and Export of Cotton,Cottonseed and Grains.
-Extensive experience in exporting into Asia especially China.
-Buyers agent for one of China's largest spinning mills.
-Capital raising from foreign investors into Australian agriculture.
-Agricultural marketing strategies for corporate and family farms.
-Importer of niche products from China.
-Array of contacts in agriculture and manufacturing in China.

Rob would like a professional business card with his company name "RT Harvestline" on the front of his business card - with contact details on the back. Preferably black and white colours.

CONTACT DETAILS THAT NEED TO BE INCLUDED:

Rob Tenwick
Mobile: 0437 615 249

Po Box 579
Kelmore QLD 4012

Email: rob@rtharvestline.com
website: www.rtharvestlin.com

```html
<!DOCTYPE html>
<html lang="en">
<head>
<meta charset="utf-8">
<title>Rob Tenwick – Business Card</title>
<link rel="stylesheet" href="https://fonts.googleapis.com/css2?family=Lato:ital,wght@0,400;0,700;1,400&display=swap">
<style>
  :root {
    --paper: #ffffff;
    --ink: #111111;
    --echo: #cbc7c4;
  }
  * { margin: 0; padding: 0; box-sizing: border-box; }
  html, body {
    width: 1200px;
    height: 741px;
    overflow: hidden;
    background: var(--paper);
  }
  .card {
    position: relative;
    width: 1200px;
    height: 741px;
    overflow: hidden;
    background: var(--paper);
    font-family: "Lato", sans-serif;
    color: var(--ink);
  }
  .name-echo,
  .name {
    position: absolute;
    top: 286px;
    font-size: 70px;
    font-weight: 700;
    line-height: 1;
    letter-spacing: 1px;
    white-space: nowrap;
    text-transform: uppercase;
  }
  .name-echo { color: var(--echo); }
  .name-echo--left { left: -9px; }
  .name-echo--right { left: 722px; }
  .name { left: 348px; color: var(--ink); }

  .contact {
    position: absolute;
    left: 350px;
    white-space: nowrap;
    line-height: 1;
    font-size: 30px;
    letter-spacing: 0.6px;
  }
  .mobile { top: 389px; font-weight: 700; letter-spacing: 1px; }
  .address-line--street { top: 470px; }
  .address-line--town { top: 511px; }
  .email { top: 591px; font-style: italic; }
  .website { top: 632px; font-style: italic; }
</style>
</head>
<body>
  <div class="card">
    <span class="name-echo name-echo--left" aria-hidden="true">Rob Tenwick</span>
    <span class="name-echo name-echo--right" aria-hidden="true">Rob Tenwick</span>
    <h1 class="name">Rob Tenwick</h1>

    <p class="contact mobile">Mobile: 0437 615 249</p>
    <p class="contact address-line address-line--street">Po Box 579</p>
    <p class="contact address-line address-line--town">Kelmore QLD 4012</p>
    <p class="contact email">Email: rob@rtharvestline.com</p>
    <p class="contact website">website: www.rtharvestlin.com</p>
  </div>
</body>
</html>
```